Monthly Mailed Newsletter/Magazine for Medical Spa

Every month we send out a mailed newsletter/magazine to our visitors from the previous month. We made a sample newsletter/magazine as a guideline of what we are looking for. We need a designer to make a simple and clean design layout.

- Attached is our sample design that has all the content we want to use.
- Newsletter/magazine is 8 pages total.
- Size of each page is 8.5 inches in width by 11 inches in height.
- Content and images can be located here: https://files.vornacloud.net/shared/8kqTRw3ZpLmX2vNcA7yHd5EbJ0sUgFo4e?view=open

The following will give you an idea of our brand presentation.
Our website is: www.GlowDermaClinic.com
Our Instagram; @glowdermaclinic
Our Facebook: www.socialtreo.com/glowdermaclinic

Target Market(s)

Women 25 - 45

Industry/Entity Type

Beauty

Font styles to use
Other font styles liked:
• Josefins Sans Bold & Lato

Colors
f78f20
ffffff

Requirements
Must have
• - Our Logo
- Our tagline: YOUR SKIN DESERVES IT!
- Address and contact information for our locations
- Our color scheme: Black and #FAA641
- Heading font is Josefin Sans Bold
- Paragraph font is Lato
- Our website address: www.GlowDermaClinic.com

```html
<!DOCTYPE html>
<html lang="en">
<head>
<meta charset="utf-8">
<title>Glow Derma Clinic – Newsletter Pages 5–7</title>
<link rel="stylesheet" href="https://fonts.googleapis.com/css2?family=Josefin+Sans:wght@700&family=Lato:ital,wght@0,400;0,700;1,700&family=Open+Sans:wght@400&display=swap">
<style>
  :root {
    --accent: #f9a43e;
    --ink: #1a1a1a;
    --paper: #ffffff;
    --board: #ffffff;
    --shadow: rgba(0,0,0,0.45);
  }
  * { box-sizing: border-box; margin: 0; padding: 0; }
  html, body { width: 1200px; height: 848px; overflow: hidden; background: var(--board); }
  .board { position: relative; width: 1200px; height: 848px; }

  .page { position: absolute; background: var(--paper); box-shadow: 5px 5px 4px var(--shadow); overflow: hidden; }
  .spread { left: 78px; top: 246px; width: 564px; height: 366px; }
  .back-page { left: 740px; top: 192px; width: 367px; height: 475px; }

  .caption { position: absolute; font-family: "Open Sans", sans-serif; font-size: 26px; color: #111; letter-spacing: 0.04em; transform: translateX(-50%); white-space: nowrap; }
  .caption-spread { left: 359px; top: 630px; }
  .caption-back { left: 931px; top: 688px; }

  .photo { position: absolute; }
  .hero-photo { left: 0; top: 0; width: 282px; height: 162px;
    background: linear-gradient(90deg, #d9d6d2 0%, #c9b6a6 45%, #8a5a40 70%, #e8e2dc 100%); }
  .sun-photo { left: 428px; top: 0; width: 136px; height: 111px;
    background: linear-gradient(180deg, #cfe3ef 0%, #f0b878 45%, #d89a76 100%); }
  .fruit-photo { left: 428px; top: 115px; width: 136px; height: 104px;
    background: radial-gradient(circle at 50% 50%, #e24b3a 0%, #f3a23a 35%, #7fae3f 55%, #f1f1f1 75%); }
  .product-photo { left: 282px; top: 263px; width: 140px; height: 103px;
    background: linear-gradient(135deg, #f3efea 0%, #e6d6c6 50%, #f5f2ee 100%); }

  .cover-title { position: absolute; left: 11px; top: 20px; font-family: "Josefin Sans", sans-serif; font-weight: 700; color: var(--accent); text-transform: uppercase; }
  .cover-title .line { display: block; font-size: 27px; line-height: 28px; }
  .cover-title .line-big { font-size: 38px; line-height: 40px; margin-top: 2px; }

  .column { position: absolute; font-family: "Lato", sans-serif; font-size: 6.1px; line-height: 7.7px; color: var(--ink); }
  .column h3 { font-family: "Lato", sans-serif; font-weight: 400; color: var(--accent); font-size: 8.6px; line-height: 10.4px; margin-bottom: 1.5px; }
  .column p { margin-bottom: 6px; }
  .column p.tight { margin-bottom: 1px; }
  .column .pick { font-weight: 700; font-style: italic; }
  .dropcap { float: left; font-size: 17px; line-height: 13px; color: var(--accent); margin-right: 1px; }

  .col-a { left: 10px; top: 169px; width: 128px; }
  .col-b { left: 144px; top: 169px; width: 128px; }
  .col-c { left: 295px; top: 10px; width: 125px; }
  .col-d { left: 428px; top: 227px; width: 128px; }

  .preview-band { position: absolute; left: 0; top: 17px; width: 367px; height: 55px; background: var(--accent);
    display: flex; align-items: center; justify-content: center; }
  .preview-band h2 { font-family: "Josefin Sans", sans-serif; font-weight: 700; color: var(--paper); font-size: 21px; letter-spacing: 0.03em; text-transform: uppercase; margin-top: 4px; }
  .mirror-photo { left: 13px; top: 88px; width: 130px; height: 186px;
    background: linear-gradient(180deg, #e9d8cf 0%, #cdb3a6 50%, #3a2a26 100%); }
  .treatment-photo { left: 162px; top: 88px; width: 191px; height: 115px;
    background: linear-gradient(90deg, #2a2424 0%, #8b6f63 50%, #d8b4a0 100%); }

  .brand { position: absolute; left: 0; top: 292px; width: 367px; display: flex; align-items: center; justify-content: center; gap: 6px; }
  .brand-dot { width: 14px; height: 14px; border-radius: 50%; background: var(--accent); }
  .brand-name { font-family: "Josefin Sans", sans-serif; font-weight: 700; font-size: 18px; color: var(--ink); margin-top: 3px; }

  .location { position: absolute; top: 362px; width: 180px; text-align: center; font-family: "Lato", sans-serif; color: var(--ink); }
  .location-yuma { left: 7px; }
  .location-tucson { left: 181px; }
  .location h4 { font-weight: 400; color: var(--accent); font-size: 10.4px; line-height: 12px; margin-bottom: 3px; }
  .location .address { font-weight: 700; font-size: 7.8px; line-height: 11.5px; }
  .location .phone { display: flex; align-items: center; justify-content: center; gap: 3px; font-weight: 700; font-size: 14px; margin-top: 6px; }
  .location .phone svg { width: 11px; height: 11px; fill: var(--ink); }

  .website { position: absolute; left: 0; top: 447px; width: 367px; text-align: center; font-family: "Lato", sans-serif; font-size: 14px; color: var(--accent); }
</style>
</head>
<body>
<div class="board">

  <section class="page spread">
    <div class="photo hero-photo" role="img" aria-label="Photo of a woman touching her forehead, checking her skin"></div>
    <h1 class="cover-title">
      <span class="line">Can you</span>
      <span class="line">make your</span>
      <span class="line">Lumitox last</span>
      <span class="line line-big">longer?</span>
    </h1>

    <div class="column col-a">
      <h3>How to Make Lumitox Results Last Longer</h3>
      <p><span class="dropcap">A</span>ging is a fact of life but looking your age isn't! "Keep calm and get Lumitox", they say. But what if the recent lockdown has rendered both impossible? Is there a way you can prolong the magical effects of expensive injections during the syringe hiatus? We sought advice board-certified advice from professionals to bring you the answer.</p>
      <h3>How Does Lumitox Work?</h3>
      <p>Lumitox reduces dynamic wrinkles but not ones caused by UV damage or gravity. Toxins from Clostridium botulinum is injected in minute amounts to block signals from nerves and cause paralysis. Lumitox only lasts for about 3 to 12 months depending on individuals.</p>
    </div>

    <div class="column col-b">
      <h3>Is it Possible to Make Lumitox and Fillers Last Longer?</h3>
      <p>Lumitox is not permanent because new nerve endings grow to stimulate muscle movement again. NY Facial plastic surgeon, Dr. Anton Veselin says that many uncontrollable factors determine how long they last. Such include variability in an individual's metabolism and immune response. Both him and dermatologist, Dr. Clara Winfield, however, agree on some simple ways to prolong the results of Lumitox.</p>
      <h3>Hydrate</h3>
      <p class="tight">A lack of elasticity in dry skin means more wrinkles. Keep your skin hydrated and moisturized.</p>
      <p class="tight">Buff your Skincare Routine</p>
      <p>A religious skincare routine is the holy-grail to healthy skin. Incorporate skin peels and collagen to speed up cell regeneration for a more youthful tone.</p>
    </div>

    <div class="column col-c">
      <h3>Use Sunscreen</h3>
      <p>Sun damage can cause premature wrinkles. Drink sufficient fluids and protect your skin with a broad-spectrum sunscreen.</p>
      <h3>Eat Right</h3>
      <p>Avoid highly processed foods and eat a balanced diet. Fresh fruits and vegetables contain antioxidants great for skin health.</p>
      <h3>Stress Less</h3>
      <p class="tight">Stress accelerates aging signs. Incorporate stress-relieving activities such as yoga and meditation to relax.</p>
      <h3>Are There Any Effective Products?</h3>
      <p>Although plastic surgeon, Dr. Helena Marsh, claims that no topical treatment that can be as effective as Lumitox, she, amongst other doctors, advocate the below to help relax wrinkles:</p>
      <p>Peptides, specifically hexapeptides.<br><span class="pick">(Recommended: Lumera Bioserum Firm at $275)</span></p>
      <p>Collagen boosting ingredients, specifically hyaluronic acid and retinol.<br><span class="pick">(Recommended: Verana Retinol Line Smoothing Night Serum Capsules at $33)</span></p>
    </div>

    <div class="photo sun-photo" role="img" aria-label="Photo of a smiling woman in a sun hat applying sunscreen at the beach"></div>
    <div class="photo fruit-photo" role="img" aria-label="Photo of a bowl of fresh fruit salad"></div>
    <div class="photo product-photo" role="img" aria-label="Photo of skincare jars and bottles on soft white fur"></div>

    <div class="column col-d">
      <h3>How Can I Be Aware of False Claims?</h3>
      <p>Many innovations on the market promise the miracle of youth. Not all are FDAapproved and backed with evidence. When in doubt, ask certified skincare professionals. Dr. Winfield is especially skeptical of radiofrequency home devices that tout anti-aging benefits. Dr. Marsh concurs and recommends that only medical-grade skincare or prescriptions should be used. &nbsp;Lumitox has replaced diamonds to become girls' best friend. We hope these tips will help you ride out the Lumitox drought till your next appointment!</p>
    </div>
  </section>

  <section class="page back-page">
    <div class="preview-band"><h2>Preview of next weeks issue</h2></div>
    <div class="photo mirror-photo" role="img" aria-label="Photo of a woman looking at her skin in a hand mirror"></div>
    <div class="photo treatment-photo" role="img" aria-label="Photo of a gloved practitioner giving a facial injection"></div>

    <div class="brand">
      <span class="brand-dot"></span>
      <span class="brand-name">Glow Derma Clinic</span>
    </div>

    <div class="location location-yuma">
      <h4>Glow Derma Clinic, Yuma, AZ</h4>
      <p class="address">1450 Palm Crest Avenue&nbsp; Suite A<br>Yuma AZ 85365</p>
      <p class="phone"><svg viewBox="0 0 24 24" aria-hidden="true"><path d="M6.6 10.8c1.4 2.8 3.8 5.1 6.6 6.6l2.2-2.2c.3-.3.7-.4 1-.2 1.1.4 2.3.6 3.6.6.6 0 1 .4 1 1V20c0 .6-.4 1-1 1C10.6 21 3 13.4 3 4c0-.6.4-1 1-1h3.5c.6 0 1 .4 1 1 0 1.3.2 2.5.6 3.6.1.3 0 .7-.2 1l-2.3 2.2z"/></svg>928-555-0148</p>
    </div>

    <div class="location location-tucson">
      <h4>Glow Derma Clinic, Tucson, AZ</h4>
      <p class="address">310 North Sage Road&nbsp; Suite 120<br>Tucson AZ 85712</p>
      <p class="phone"><svg viewBox="0 0 24 24" aria-hidden="true"><path d="M6.6 10.8c1.4 2.8 3.8 5.1 6.6 6.6l2.2-2.2c.3-.3.7-.4 1-.2 1.1.4 2.3.6 3.6.6.6 0 1 .4 1 1V20c0 .6-.4 1-1 1C10.6 21 3 13.4 3 4c0-.6.4-1 1-1h3.5c.6 0 1 .4 1 1 0 1.3.2 2.5.6 3.6.1.3 0 .7-.2 1l-2.3 2.2z"/></svg>520-555-0192</p>
    </div>

    <p class="website">www.GlowDermaClinic.com</p>
  </section>

  <p class="caption caption-spread">Pages 5 &amp; 6 spread</p>
  <p class="caption caption-back">Page 7</p>
</div>
</body>
</html>
```